Business Card for: Northbrook Financial Advisory Services Inc.

provide strategic financial advisory services to companies in the areas of corporate finance, mergers and acquisitions, executive coaching and strategic planning

Target Market(s)

Companies, banks, accountants, lawyers

Industry/Entity Type

High end business consulting in corporate finance, mergers and acquisitions, consulting

Contact Information for Business Card

Name of company, Name: xxxxxx xxxxxx , CEO, - phone number: 1-xxx-xxx-xxxx, - email address,

Requirements
Must have
• Must be professional and simple.
Nice to have
• simple, straight graphics, must give the impression that we are trustworthy, professional, competent
Should not have
• loud colors, loud design features

```html
<!DOCTYPE html>
<html lang="en">
<head>
<meta charset="utf-8">
<title>Northbrook Financial Advisory Services Inc. – Business Card</title>
<link rel="stylesheet" href="https://fonts.googleapis.com/css2?family=Roboto:wght@400&family=Roboto+Condensed:ital,wght@1,700&display=swap">
<style>
  :root {
    --backdrop: #757575;
    --card: #ffffff;
    --accent: #f7941d;
    --blue-light: #29abe2;
    --blue-dark: #2e3192;
    --ink: #111111;
    --on-blue: #ffffff;
  }
  html, body {
    margin: 0;
    padding: 0;
    width: 1199px;
    height: 1200px;
    overflow: hidden;
    background: var(--backdrop);
  }
  .sheet {
    position: absolute;
    left: 0;
    top: 0;
    width: 960px;
    height: 961px;
    transform: scale(1.249);
    transform-origin: 0 0;
  }
  .card {
    position: absolute;
    left: 122px;
    width: 716px;
    height: 419px;
    background: var(--card);
    overflow: hidden;
    box-shadow: 8px 10px 14px rgba(0, 0, 0, 0.35);
  }
  .card--front { top: 47px; }
  .card--back { top: 496px; }
  .card__shapes {
    position: absolute;
    inset: 0;
    width: 716px;
    height: 419px;
  }
  .company-name {
    position: absolute;
    margin: 0;
    font-family: "Roboto Condensed", "Arial Narrow", sans-serif;
    font-style: italic;
    font-weight: 700;
    font-size: 29px;
    line-height: 1;
    color: var(--accent);
    white-space: nowrap;
  }
  .card--front .company-name { left: 56px; top: 66px; }
  .card--back .company-name { left: 0; right: 0; top: 193px; text-align: center; }
  .person {
    position: absolute;
    left: 55px;
    top: 208px;
    color: var(--on-blue);
    font-family: "Roboto", Arial, sans-serif;
  }
  .person__name { margin: 0; font-size: 30px; font-weight: 400; line-height: 1; }
  .person__title { margin: 8px 0 0; font-size: 16px; line-height: 1; }
  .contact-list {
    position: absolute;
    margin: 0;
    padding: 0;
    list-style: none;
    font-family: "Roboto", Arial, sans-serif;
    font-size: 18px;
    line-height: 28px;
  }
  .contact-list--direct { left: 55px; top: 302px; color: var(--on-blue); }
  .contact-list--address { left: 404px; top: 302px; color: var(--ink); }
  .contact-list li { position: relative; padding-left: 26px; }
  .contact-icon {
    position: absolute;
    left: 0;
    top: 8px;
    width: 12px;
    height: 12px;
    fill: currentColor;
  }
</style>
</head>
<body>
<main class="sheet">

  <section class="card card--front" aria-label="Business card front">
    <svg class="card__shapes" viewBox="0 0 716 419" aria-hidden="true">
      <defs>
        <linearGradient id="tile-gradient" x1="0" y1="0.15" x2="1" y2="0.85">
          <stop offset="0" stop-color="var(--blue-light)" style="stop-color:#29abe2"/>
          <stop offset="1" stop-color="var(--blue-dark)" style="stop-color:#2e3192"/>
        </linearGradient>
      </defs>
      <rect x="-155" y="-155" width="310" height="310" rx="46" fill="url(#tile-gradient)" transform="translate(143 323) rotate(45)"/>
      <rect x="-30" y="-30" width="60" height="60" rx="12" fill="url(#tile-gradient)" transform="translate(315 209) rotate(45)"/>
      <rect x="-110" y="-110" width="220" height="220" rx="34" fill="url(#tile-gradient)" transform="translate(714 203) rotate(45)"/>
    </svg>

    <h1 class="company-name">Northbrook Financial Advisory Services Inc.</h1>

    <div class="person">
      <p class="person__name">Dana Whitfield</p>
      <p class="person__title">CEO</p>
    </div>

    <ul class="contact-list contact-list--direct">
      <li>
        <svg class="contact-icon" viewBox="0 0 24 24" aria-hidden="true"><path d="M6.6 10.8a15.1 15.1 0 0 0 6.6 6.6l2.2-2.2a1 1 0 0 1 1-.25 11.4 11.4 0 0 0 3.6.57 1 1 0 0 1 1 1V20a1 1 0 0 1-1 1A17 17 0 0 1 3 4a1 1 0 0 1 1-1h3.5a1 1 0 0 1 1 1c0 1.25.2 2.45.57 3.57a1 1 0 0 1-.25 1z"/></svg>
        832-555-0147
      </li>
      <li>
        <svg class="contact-icon" viewBox="0 0 24 24" aria-hidden="true"><path d="M20 4H4a2 2 0 0 0-2 2v12a2 2 0 0 0 2 2h16a2 2 0 0 0 2-2V6a2 2 0 0 0-2-2zm0 4-8 5-8-5V6l8 5 8-5z"/></svg>
        info@northbrookfa.com
      </li>
    </ul>

    <ul class="contact-list contact-list--address">
      <li>
        <svg class="contact-icon" viewBox="0 0 24 24" aria-hidden="true" style="left:-2px;top:5px"><path d="M12 2a7 7 0 0 0-7 7c0 5.25 7 13 7 13s7-7.75 7-13a7 7 0 0 0-7-7zm0 9.5A2.5 2.5 0 1 1 12 6.5a2.5 2.5 0 0 1 0 5z"/></svg>
        298/A, Address, Street,<br>Pincode-123456
      </li>
    </ul>
  </section>

  <section class="card card--back" aria-label="Business card back">
    <svg class="card__shapes" viewBox="0 0 716 419" aria-hidden="true">
      <defs>
        <linearGradient id="tile-gradient-back" x1="0" y1="0.15" x2="1" y2="0.85">
          <stop offset="0" style="stop-color:#29abe2"/>
          <stop offset="1" style="stop-color:#2e3192"/>
        </linearGradient>
      </defs>
      <rect x="-88" y="-88" width="176" height="176" rx="32" fill="url(#tile-gradient-back)" transform="translate(577 -17) rotate(45)"/>
      <rect x="-30" y="-30" width="60" height="60" rx="12" fill="url(#tile-gradient-back)" transform="translate(427 97) rotate(45)"/>
      <rect x="-140" y="-140" width="280" height="280" rx="52" fill="url(#tile-gradient-back)" transform="translate(70 458) rotate(45)"/>
      <rect x="-30" y="-30" width="60" height="60" rx="12" fill="url(#tile-gradient-back)" transform="translate(241 372) rotate(45)"/>
    </svg>

    <h2 class="company-name">Northbrook Financial Advisory Services Inc.</h2>
  </section>

</main>
</body>
</html>
```